Adlinks Landing Page - DESIGN ONLY! PSD File

BACKGROUND:
Our website www.trailkit.com.au (running on Storlane) has a range of outdoor equipment being sold online. One of the products we specialize in is generators.
We are after a content landing page designed for Bluefin Adlinks to link to. This page should be focused on converting customers to sales as most customers at this stage of buying are ready to buy. We would like this page to focus on a combination of a professional graphic design and some text. The way it is laid out is open to your own experience, we just want it to look professional and have the right info for customers to convert.
THE BRIEF:
The page will include the range of products in the generator category that can be found here:
http://www.trailkit.com.au/generators.html
This page should include all the products within this category and should fit into to the color scheme and look of the website.
Most focus on the product should be placed in this order of priority, with special focus on the first two:
1. 2kva RRP: $1099 down to $499
2. 3.5kva RRP: $1399 down to $780
3. 3.5kva electric start RRP: $1599 down to $890
4. 4.4kva RRP: $1899 down to $950 (not currently listed, images will be provided soon)
5. 5kva RRP: $1999 down to $1150
The page can include a variety of graphic design, text and hyperlinks (or image clickable links), so please take this into account when making the graphics design.
The page must be discount oriented and include prices of each product as well as its original RRP price (crossed out), possible 'sale' graphics, and 'buy now' buttons linking to the product.
An example area this should fit within is the the column the products are on this page:
Other notes:
Our prices are truly bargains and the lowest in the market, so don't be afraid to express that in the design; texts like "Massive Sale" , "Priced to Clear Out" , "Won't Last Long at this Price"
Product images can be grabbed off the products here:
Deliverable will be a PSD file of the finished design.
We need these contact numbers included somewhere on this page:
NSW/ACT: 02 8555 0142
VIC/TAS: 03 9555 0176
SA: 08 7555 0193
NT/WA: 08 85550127

```html
<!DOCTYPE html>
<html lang="en">
<head>
<meta charset="utf-8">
<title>TrailKit Generators – Lowest Price in the Market</title>
<link rel="stylesheet" href="https://fonts.googleapis.com/css2?family=Open+Sans:wght@400;600;700&display=swap">
<style>
  :root {
    --earth-light: #c9a77c;
    --earth-mid: #9a7550;
    --earth-dark: #5a3f27;
    --band-dark: rgba(28, 26, 24, 0.82);
    --text-white: #ffffff;
    --text-soft: #e6e2dc;
    --text-grey: #b9b6b2;
    --price-green: #2bd62b;
    --strike-red: #e0201e;
    --title-red: #e8201c;
    --btn-green-top: #5cd65a;
    --btn-green-bottom: #1f9a22;
    --btn-blue-top: #5fb8ea;
    --btn-blue-bottom: #1f78b8;
    --btn-dark-top: #5a5856;
    --btn-dark-bottom: #2a2928;
    --btn-orange-top: #ff8a3a;
    --btn-orange-bottom: #d9480c;
    --field-bg: #141312;
    --divider: rgba(255, 255, 255, 0.18);
    --photo-red: #c9231f;
    --photo-dark: #3a2222;
  }
  * { margin: 0; padding: 0; box-sizing: border-box; }
  html, body { width: 1200px; height: 1200px; overflow: hidden; }
  body {
    position: relative;
    font-family: "Open Sans", "Segoe UI", sans-serif;
    color: var(--text-white);
  }
  .ground {
    position: absolute; inset: 0;
    background:
      radial-gradient(ellipse 45% 12% at 50% 62%, rgba(255,240,215,0.55), transparent 70%),
      radial-gradient(ellipse 70% 60% at 50% 45%, var(--earth-light), var(--earth-mid) 60%, var(--earth-dark));
  }
  .abs { position: absolute; }

  /* Header */
  .brand { left: 258px; top: 36px; font-size: 30px; font-weight: 700; color: #1c1a18; letter-spacing: 0.5px; }
  .header-rule { height: 1px; background: rgba(40,30,20,0.55); }
  .main-nav { left: 250px; top: 105px; font-size: 12px; letter-spacing: -0.1px; }
  .main-nav a { color: var(--text-white); text-decoration: none; position: absolute; white-space: nowrap; }
  .field {
    width: 182px; height: 23px; border-radius: 5px;
    background: var(--field-bg); border: 1px solid #5a5654;
    font-size: 12px; font-style: italic; color: #77736f; padding: 3px 15px;
  }
  .btn {
    display: flex; align-items: center; justify-content: center;
    border-radius: 3px; font-size: 12px; font-weight: 600; color: var(--text-white);
    text-decoration: none; box-shadow: 0 1px 2px rgba(0,0,0,0.5); white-space: nowrap;
  }
  .btn-blue { background: linear-gradient(var(--btn-blue-top), var(--btn-blue-bottom)); width: 57px; height: 25px; }
  .btn-green { background: linear-gradient(var(--btn-green-top), var(--btn-green-bottom)); width: 74px; height: 25px; }
  .btn-dark { background: linear-gradient(var(--btn-dark-top), var(--btn-dark-bottom)); width: 74px; height: 25px; font-weight: 400; }
  .btn-orange { background: linear-gradient(var(--btn-orange-top), var(--btn-orange-bottom)); width: 73px; height: 25px; }
  .member-note { left: 785px; top: 106px; font-size: 12px; letter-spacing: -0.2px; white-space: nowrap; }

  /* Hero band */
  .band { left: 0; width: 1200px; background: var(--band-dark); }
  .hero-title { left: 0; width: 1200px; top: 146px; text-align: center; font-size: 50px; font-weight: 400; white-space: nowrap; }
  .hero-sub { left: 0; width: 1200px; top: 204px; text-align: center; font-size: 16px; font-weight: 600; }
  .hero-copy {
    left: 245px; width: 710px; top: 228px;
    font-size: 11.6px; letter-spacing: -0.15px; line-height: 20.7px; text-align: center; color: var(--text-soft);
  }
  .feature-panel {
    left: 250px; top: 298px; width: 700px; height: 420px;
    background: radial-gradient(ellipse 60% 70% at 50% 45%, rgba(90,88,86,0.9), rgba(60,58,56,0.6) 70%, transparent);
  }
  .divider-v { width: 1px; background: var(--divider); }

  .photo { border-radius: 18px 30px 10px 10px;
    background: radial-gradient(ellipse at 55% 40%, var(--photo-red), #8a1512 75%, var(--photo-dark)); }
  .featured-title { font-size: 20.5px; line-height: 25px; font-weight: 400; white-space: nowrap; }
  .price-regular { font-size: 14.5px; color: var(--text-grey); white-space: nowrap; }
  .price-regular s { text-decoration-color: var(--strike-red); }
  .price-special { font-size: 14.5px; color: var(--price-green); white-space: nowrap; }
  .featured-copy { width: 168px; font-size: 11.6px; line-height: 12.5px; color: var(--text-soft); height: 76px; overflow: hidden; }

  .range-title { font-size: 12px; line-height: 16.7px; color: var(--title-red); font-weight: 600; white-space: nowrap; }
  .range-regular { font-size: 12px; color: var(--text-grey); white-space: nowrap; }
  .range-regular s { text-decoration-color: var(--strike-red); }
  .range-special { font-size: 12px; color: var(--price-green); white-space: nowrap; }

  /* Footer */
  .footer-head { font-size: 12.5px; font-weight: 400; }
  .footer-copy { font-size: 10px; line-height: 12.5px; color: var(--text-soft); }
</style>
</head>
<body>
  <div class="ground" role="img" aria-label="Cracked dry earth texture in warm browns"></div>

  <header>
    <div class="abs brand">TrailKit</div>
    <div class="abs header-rule" style="left:250px; top:93px; width:182px;"></div>
    <nav class="abs main-nav">
      <a href="#" style="left:0">Home</a>
      <a href="#" style="left:75px">Featured Products</a>
      <a href="#" style="left:213px">Pricing</a>
      <a href="#" style="left:288px">About Us</a>
      <a href="#" style="left:377px">Help</a>
    </nav>
    <div class="abs field" style="left:768px; top:9px;">Username or email</div>
    <div class="abs field" style="left:768px; top:35px;">Password</div>
    <a class="abs btn btn-blue" href="#" style="left:893px; top:63px;">Log In</a>
    <div class="abs header-rule" style="left:768px; top:93px; width:182px;"></div>
    <div class="abs member-note">Not a member yet</div>
    <a class="abs btn btn-blue" href="#" style="left:893px; top:99px;">Sign Up</a>
  </header>

  <section class="abs band" style="top:130px; height:588px;"></section>
  <div class="abs feature-panel"></div>
  <h1 class="abs hero-title">Lowest Price in the market</h1>
  <p class="abs hero-sub">grab this opportunity &amp; make your life better.</p>
  <p class="abs hero-copy">This is Pixelform's version &nbsp;of Lorem Ipsum. Proin gravida nibh vel velit auctor aliquet. Aenean sollicitudin, lorem quis bibendum auctor, nisi elit consequat ipsum, nec sagittis sem nibh id elit. Duis sed odio sit amet nibh vulputate cursus a sit amet mauris. Morbi accumsan ipsum velit. Nam nec tellus a odio tincidunt auctor a ornare odio. Sed non &nbsp;mauris vitae erat conse-</p>

  <div class="abs divider-v" style="left:603px; top:350px; height:360px;"></div>

  <article>
    <div class="abs photo" style="left:288px; top:312px; width:204px; height:218px;" role="img" aria-label="Red 2kVA inverter generator product photo"></div>
    <h2 class="abs featured-title" style="left:250px; top:549px;">Silent 2kVA Pure Sine<br>Wave Inverter Generator</h2>
    <div class="abs price-regular" style="left:250px; top:597px;">Regular Price: <s>$1,099.00</s></div>
    <div class="abs price-special" style="left:250px; top:613px;">Special Price: $499.00</div>
    <a class="abs btn btn-green" href="#" style="left:423px; top:605px;">Buy Now</a>
    <p class="abs featured-copy" style="left:250px; top:637px;">Features - This is Pixelform's version &nbsp;of Lorem Ipsum. Proin gravida nibh vel velit auctor aliquet. Aenean sollicitudin, lorem quis bibendum auctor, nisi elit consequat ipsum, nec</p>
    <a class="abs btn btn-dark" href="#" style="left:423px; top:690px;">View More</a>
  </article>

  <article>
    <div class="abs photo" style="left:688px; top:312px; width:202px; height:218px;" role="img" aria-label="Red 3.5kVA inverter generator product photo"></div>
    <h2 class="abs featured-title" style="left:649px; top:550px;">Silent 3.5kVA Pure Sine<br>Wave Inverter Generator</h2>
    <div class="abs price-regular" style="left:649px; top:597px;">Regular Price: <s>$1,399.00</s></div>
    <div class="abs price-special" style="left:649px; top:613px;">Special Price: $780.00</div>
    <a class="abs btn btn-green" href="#" style="left:822px; top:605px;">Buy Now</a>
    <p class="abs featured-copy" style="left:649px; top:637px;">Features - This is Pixelform's version &nbsp;of Lorem Ipsum. Proin gravida nibh vel velit auctor aliquet. Aenean sollicitudin, lorem quis bibendum auctor, nisi elit consequat ipsum, nec</p>
    <a class="abs btn btn-dark" href="#" style="left:822px; top:690px;">View More</a>
  </article>

  <section class="abs band" style="top:780px; height:277px;"></section>
  <div class="abs divider-v" style="left:471px; top:820px; height:220px;"></div>
  <div class="abs divider-v" style="left:745px; top:820px; height:220px;"></div>

  <article>
    <div class="abs photo" style="left:254px; top:798px; width:126px; height:116px;" role="img" aria-label="Red 3.5kVA electric start generator product photo"></div>
    <h3 class="abs range-title" style="left:250px; top:925px;">Silent 3.5kVA Pure Sine Wave<br>Inverter Generator<br>Electric Start + Remote</h3>
    <div class="abs range-regular" style="left:249px; top:980px;">Regular Price: <s>$1,599.00</s></div>
    <div class="abs range-special" style="left:249px; top:997px;">Special Price: $890.00</div>
    <a class="abs btn btn-orange" href="#" style="left:288px; top:1019px;">Buy Now</a>
  </article>

  <article>
    <div class="abs photo" style="left:553px; top:793px; width:116px; height:122px;" role="img" aria-label="Red 4.4kVA inverter generator product photo"></div>
    <h3 class="abs range-title" style="left:531px; top:925px;">Silent 4.4kVA Pure Sine<br>Wave Inverter Generator<br>Electric Start + Remote</h3>
    <div class="abs range-regular" style="left:530px; top:980px;">Regular Price: <s>$1,899.00</s></div>
    <div class="abs range-special" style="left:530px; top:997px;">Special Price: $950.00</div>
    <a class="abs btn btn-orange" href="#" style="left:568px; top:1019px;">Buy Now</a>
  </article>

  <article>
    <div class="abs photo" style="left:822px; top:798px; width:118px; height:118px; background:linear-gradient(90deg,#1e1e1e 55%,var(--photo-red) 56%);" role="img" aria-label="Black and red 5kVA inverter generator product photo"></div>
    <h3 class="abs range-title" style="left:808px; top:925px;">Silent 5kVA Pure Sine<br>Wave Inverter Generator<br>&nbsp;Electric Start + Remote</h3>
    <div class="abs range-regular" style="left:807px; top:980px;">Regular Price: <s>$1,999.00</s></div>
    <div class="abs range-special" style="left:807px; top:997px;">Special Price: $1150.00</div>
    <a class="abs btn btn-orange" href="#" style="left:843px; top:1019px;">Buy Now</a>
  </article>

  <footer>
    <div class="abs header-rule" style="left:340px; top:1096px; width:700px; background:rgba(255,255,255,0.25);"></div>
    <h4 class="abs footer-head" style="left:249px; top:1110px;">Generators</h4>
    <p class="abs footer-copy" style="left:249px; top:1133px; width:120px;">This is Pixelform's version &nbsp;of Lorem Ipsum. Proin gravida nibh vel velit auctor aliquet. Aenean sollicitudin,</p>
    <h4 class="abs footer-head" style="left:398px; top:1110px;">Winches</h4>
    <p class="abs footer-copy" style="left:390px; top:1133px; width:80px;">This is Pixel-<br>form's version<br>of Lorem Ipsum.<br>Proin gravida<br>nibh vel velit</p>
    <h4 class="abs footer-head" style="left:520px; top:1110px;">Tents</h4>
    <p class="abs footer-copy" style="left:505px; top:1133px; width:80px;">This is Pixel-<br>form's version<br>of Lorem Ipsum.<br>Proin gravida<br>nibh vel velit</p>
    <h4 class="abs footer-head" style="left:624px; top:1110px;">Jacks</h4>
    <p class="abs footer-copy" style="left:617px; top:1133px; width:80px;">This is Pixel-<br>form's version<br>of Lorem Ipsum.<br>Proin gravida<br>nibh vel velit</p>
    <h4 class="abs footer-head" style="left:837px; top:1110px;">Contact Us</h4>
    <p class="abs footer-copy" style="left:838px; top:1142px; width:140px; font-size:10.3px;">NSW/ACT: 02 8555 0142<br>VIC/TAS: 03 9555 0176<br>SA: 08 7555 0193<br>NT/WA: 08 85550127</p>
  </footer>
</body>
</html>
```